Folded Business Cards for Guarantee, Layaway & The Fine Print

I am looking for a set of (3) folded business for our guarantee, layaway and fine print policies. I would like the same design for each of these cards, with the exception of the picture, title and verbiage.
The front of each card must include our logo, the title of the card (Our Guarantee, Layaway or The Fine Print,) and a picture of a piece of jewelry. The inside of the card should state our policies. The back of the card should have our logo, address (Bellstone Court #9, Maplecrest, NH 03999,) phone # (555-281-0947) email & web address (info@vantorgems.com, www.vantorgems.com) and social media icons (FB, Twitter, Pinterest, Instagram)

The layaway card needs a place for the customer's signature.

I was thinking the orientation of the card should be vertical but if the right design ends up being horizontal, I'm ok with that. I do have concerns about readability and that this may be too much information for a folded business card. So, I am open to either changing the front & back, if need be or going to a different format (standard postcard size. Verbiage may also need to be trimmed down, but I need to know what is possible first.

Our branding colors are espresso brown & coppery orange so please do not stray from this color palette. The font of our logo is joefin. I would like the verbiage of the cards to be in quattrocento sans font. We would like a modern & clean look please.

Attached, please find our logo, policies and jewelry pictures. For picture placement, please do the following: Layaway Card (Quartz & onyx pendant,) The Fine Print Card (Orange Garnet Pendant,) Our Guarantee (triple Green Tourmaline Ring.)

```html
<!DOCTYPE html>
<html lang="en">
<head>
<meta charset="utf-8">
<title>Vantor's Layaway Card</title>
<link rel="stylesheet" href="https://fonts.googleapis.com/css2?family=Quattrocento:wght@400;700&display=swap">
<style>
  :root {
    --copper: #c44e04;
    --espresso: #4f2601;
    --copper-text: #b5520f;
    --page: #ffffff;
  }
  * { margin: 0; padding: 0; box-sizing: border-box; }
  html, body { width: 1200px; height: 900px; overflow: hidden; background: var(--page); }
  .canvas { position: relative; width: 1200px; height: 900px; }
  .card { position: absolute; left: 111px; top: 16px; width: 978px; height: 864px; background: var(--espresso); }
  .band { position: absolute; left: 111px; width: 978px; background: var(--copper); }
  .band--top { top: 16px; height: 69px; }
  .band--bottom { top: 810px; height: 70px; }
  .brand, .title, .contact {
    position: absolute; color: var(--copper-text); white-space: nowrap;
    font-family: "Quattrocento", serif;
  }
  .brand { font-weight: 400; line-height: 1; }
  .brand--back { left: 222px; top: 200px; font-size: 74px; }
  .brand--front { left: 612px; top: 515px; font-size: 104px; }
  .contact { font-weight: 700; font-size: 30px; line-height: 1; }
  .rule { position: absolute; height: 2px; background: var(--copper-text); }
  .social { position: absolute; top: 625px; left: 199px; display: flex; gap: 15px; }
  .social span { width: 80px; height: 80px; border-radius: 14px; background: var(--copper-text); display: block; }
  .pendant { position: absolute; left: 700px; top: 16px; width: 245px; height: 470px; }
  .title { left: 662px; top: 688px; font-size: 70px; line-height: 1; font-weight: 400; }
</style>
</head>
<body>
<div class="canvas">
  <div class="card"></div>
  <div class="band band--top"></div>
  <div class="band band--bottom"></div>

  <svg class="pendant" role="img" aria-label="Photo of a rutilated quartz and onyx pendant in gold on a fine chain" viewBox="0 0 245 470">
    <defs>
      <linearGradient id="pendant-tone" x1="0" y1="0" x2="0" y2="1">
        <stop offset="0" stop-color="#c9a23a" stop-opacity="0.35"/>
        <stop offset="0.45" stop-color="#8a5a2a" stop-opacity="0.6"/>
        <stop offset="1" stop-color="#140a04" stop-opacity="0.85"/>
      </linearGradient>
    </defs>
    <rect width="245" height="470" rx="10" fill="url(#pendant-tone)"/>
  </svg>

  <div class="brand brand--back">Vantor's</div>
  <div class="rule" style="left:265px;top:342px;width:237px;"></div>

  <div class="contact" style="left:187px;top:356px;">Bellstone Court #9,</div>
  <div class="contact" style="left:187px;top:404px;">Maplecrest, NH 03999</div>
  <div class="rule" style="left:265px;top:451px;width:237px;"></div>
  <div class="contact" style="left:269px;top:459px;">555-281-0947</div>
  <div class="rule" style="left:265px;top:501px;width:237px;"></div>
  <div class="contact" style="left:177px;top:515px;">info@vantorgems.com</div>
  <div class="contact" style="left:177px;top:562px;">www.vantorgems.com</div>
  <div class="rule" style="left:265px;top:607px;width:237px;"></div>

  <div class="social" aria-label="Social media links">
    <span></span><span></span><span></span><span></span>
  </div>

  <div class="brand brand--front">Vantor's</div>
  <div class="rule" style="left:658px;top:681px;width:330px;"></div>
  <div class="title">Layaway</div>
  <div class="rule" style="left:658px;top:770px;width:330px;"></div>
</div>
</body>
</html>
```